Software Company Business Card

We are looking for a new design of our business card. The design will also be used in the rest of our branding and marketing materials as we want to keep it all uniform. We sell POS software to fine/luxury jewelers and also offer other business services as well to help the jeweler manage their business and need something more updated, technical and fresh, preferably more on the masculine side. We do not want any designs with gems in them but if possible would like to incorporate the circle and arrow in the logo into the design, but not a requirement if you can't make it work. I would like to see a variety of the mix. The colors need to remain our blue and orange and the logo can not change. The squiggly lines have been used as our corporate identity for over 20 years and its time to update. Our company name is PELK (Bright Ledger Counter Solutions).

Target Market(s)

High End Jewelers

Industry/Entity Type

Software

Contact Information for Business Card

Requirements
Must have
• Our logo and the colors must remain the same. Blue is #d95d39 and Orange is #0f5682.
Nice to have
• The circle and arrow incorporated but not a requirement.
Should not have
• Anything jewelry or gem related.

```html
<!DOCTYPE html>
<html lang="en">
<head>
<meta charset="utf-8">
<title>PELK Business Card</title>
<link href="https://fonts.googleapis.com/css2?family=Montserrat:wght@300;400;600;700&display=swap" rel="stylesheet">
<style>
  :root {
    --brand-blue: #0f5682;
    --brand-orange: #d95d39;
    --backdrop: #07487f;
    --card: #f7f7f7;
    --ink: #4a4a4a;
    --rule: #b5b5b5;
  }
  * { margin: 0; padding: 0; box-sizing: border-box; }
  html, body { width: 1200px; height: 1170px; overflow: hidden; }
  body {
    background: var(--backdrop);
    font-family: "Montserrat", sans-serif;
    position: relative;
  }
  .card {
    position: absolute;
    left: 170px;
    width: 860px;
    height: 491px;
    background: var(--card);
    box-shadow: 0 12px 30px rgba(0, 0, 0, 0.25);
  }
  .card--front { top: 70px; }
  .card--back { top: 609px; }

  .company-name {
    font-weight: 600;
    color: var(--brand-blue);
    line-height: 1;
    letter-spacing: 8px;
    text-transform: uppercase;
  }
  .card--front .company-name {
    position: absolute;
    left: 60px;
    top: 212px;
    font-size: 52px;
  }

  .divider {
    position: absolute;
    left: 382px;
    top: 142px;
    width: 1px;
    height: 200px;
    background: var(--rule);
  }

  .contact {
    position: absolute;
    left: 420px;
    top: 112px;
  }
  .contact__name {
    font-weight: 700;
    font-size: 36px;
    color: var(--brand-blue);
    letter-spacing: 0.3px;
  }
  .contact__role {
    font-weight: 400;
    font-size: 16px;
    color: var(--brand-orange);
    margin-top: 2px;
  }
  .contact__list {
    list-style: none;
    margin-top: 26px;
  }
  .contact__item {
    display: flex;
    align-items: flex-start;
    gap: 22px;
    font-size: 17px;
    color: var(--ink);
    line-height: 1.25;
    margin-bottom: 8px;
  }
  .contact__icon {
    width: 14px;
    height: 14px;
    margin-top: 3px;
    fill: var(--brand-orange);
    flex-shrink: 0;
  }

  .card--back .company-name {
    position: absolute;
    left: 50%;
    top: 50%;
    transform: translate(-50%, -50%);
    font-size: 72px;
    letter-spacing: 12px;
  }
</style>
</head>
<body>
  <section class="card card--front">
    <p class="company-name">Pelk</p>
    <div class="divider"></div>
    <div class="contact">
      <h1 class="contact__name">Dorian Vance</h1>
      <p class="contact__role">Director of Global Operation</p>
      <ul class="contact__list">
        <li class="contact__item">
          <svg class="contact__icon" viewBox="0 0 24 24"><path d="M6.6 10.8a15.1 15.1 0 0 0 6.6 6.6l2.2-2.2a1 1 0 0 1 1-.25 11.4 11.4 0 0 0 3.6.57 1 1 0 0 1 1 1V20a1 1 0 0 1-1 1A17 17 0 0 1 3 4a1 1 0 0 1 1-1h3.5a1 1 0 0 1 1 1c0 1.25.2 2.45.57 3.57a1 1 0 0 1-.25 1z"/></svg>
          <span>+1 800 555 0142</span>
        </li>
        <li class="contact__item">
          <svg class="contact__icon" viewBox="0 0 24 24"><path d="M7 2h10a2 2 0 0 1 2 2v16a2 2 0 0 1-2 2H7a2 2 0 0 1-2-2V4a2 2 0 0 1 2-2zm0 3v11h10V5zm5 13a1.2 1.2 0 1 0 0 2.4 1.2 1.2 0 0 0 0-2.4z"/></svg>
          <span>+1 703 555 0187</span>
        </li>
        <li class="contact__item">
          <svg class="contact__icon" viewBox="0 0 24 24"><path d="M12 2a10 10 0 1 0 5 18.7l-1-1.7A8 8 0 1 1 20 12v1.2a1.8 1.8 0 0 1-3.6 0V7.5h-2v.9A4.5 4.5 0 1 0 15 15.6a3.8 3.8 0 0 0 7-2.4V12A10 10 0 0 0 12 2zm0 12.6a2.6 2.6 0 1 1 0-5.2 2.6 2.6 0 0 1 0 5.2z"/></svg>
          <span>dorian@pelkco.com</span>
        </li>
        <li class="contact__item">
          <svg class="contact__icon" viewBox="0 0 24 24"><path d="M12 2a10 10 0 1 0 0 20 10 10 0 0 0 0-20zm6.9 6h-2.9a15 15 0 0 0-1.4-3.6A8 8 0 0 1 18.9 8zM12 4c.8 1.2 1.5 2.5 1.9 4h-3.8c.4-1.5 1.1-2.8 1.9-4zM4.3 14a8 8 0 0 1 0-4h3.4a16 16 0 0 0 0 4zm.8 2h2.9a15 15 0 0 0 1.4 3.6A8 8 0 0 1 5.1 16zM8 8H5.1a8 8 0 0 1 4.3-3.6A15 15 0 0 0 8 8zm4 12c-.8-1.2-1.5-2.5-1.9-4h3.8c-.4 1.5-1.1 2.8-1.9 4zm2.3-6H9.7a14 14 0 0 1 0-4h4.6a14 14 0 0 1 0 4zm.3 5.6A15 15 0 0 0 16 16h2.9a8 8 0 0 1-4.3 3.6zM16.3 14a16 16 0 0 0 0-4h3.4a8 8 0 0 1 0 4z"/></svg>
          <span>www.pelkco.com</span>
        </li>
        <li class="contact__item">
          <svg class="contact__icon" viewBox="0 0 24 24"><path d="M12 2a7 7 0 0 0-7 7c0 5.2 7 13 7 13s7-7.8 7-13a7 7 0 0 0-7-7zm0 9.5a2.5 2.5 0 1 1 0-5 2.5 2.5 0 0 1 0 5z"/></svg>
          <span>1480 Harbor Loop Suite 210<br>Larkfield, CO 80912 USA</span>
        </li>
      </ul>
    </div>
  </section>

  <section class="card card--back">
    <p class="company-name">Pelk</p>
  </section>
</body>
</html>
```